Kestrel Fitness Personal Training Business

I need a business card design with a logo for my personal training company. I'd like the colors to be a vibrant green and black. I'd like the logo to incorporate an anvil (or something similar). I train hardcore competitive athletes as well as soccer moms trying to get and/or stay in shape. I need a logo that will not pigeon hole me in one category or the other, but at the same time not be too intimidating to soccer moms, but will not be off putting to the more hardcore trainees. The design should be attention grabbing and aesthetic.
Target Market(s)
Hardcore athletes as well as average people just trying to get/stay in shape.
Industry/Entity Type
Training
Look and feel
Each slider illustrates characteristics of the customer's brand and the style your logo design should communicate.

```html
<!DOCTYPE html>
<html lang="en">
<head>
<meta charset="utf-8">
<title>Kestrel Fitness – Business Card</title>
<link href="https://fonts.googleapis.com/css2?family=Open+Sans:wght@400;600;800&display=swap" rel="stylesheet">
<style>
  :root {
    --bg: #9a9a98;
    --card-black: #060606;
    --strip-dark: #141414;
    --green: #0aa64c;
    --green-light: #5cc54a;
    --green-text: #3dbd4c;
    --white: #f4f4f4;
    --ghost: rgba(70, 70, 70, 0.35);
  }
  * { box-sizing: border-box; margin: 0; padding: 0; }
  html, body {
    width: 1200px; height: 900px; overflow: hidden;
    background: var(--bg);
    font-family: "Open Sans", Arial, sans-serif;
  }
  .canvas {
    width: 1200px; height: 900px;
    display: flex; flex-direction: column; align-items: center; justify-content: center;
    gap: 44px;
  }
  .card {
    position: relative;
    width: 660px; height: 377px;
    background: var(--card-black);
    overflow: hidden;
    box-shadow: 0 6px 18px rgba(0,0,0,0.25);
  }
  .card__ghost {
    position: absolute;
    background: radial-gradient(ellipse at center, var(--ghost) 0%, rgba(40,40,40,0.15) 55%, transparent 75%);
  }
  .card__band {
    position: absolute; left: 0; right: 0; bottom: 0;
    background: var(--green);
    border-top: 8px solid var(--green-light);
  }
  .card__band::after {
    content: ""; position: absolute; left: 0; right: 0; bottom: 0; height: 7px;
    background: var(--green-light);
  }

  /* Front */
  .front .card__ghost { right: -20px; top: 50px; width: 230px; height: 250px; }
  .front .card__band { height: 96px; }
  .brand {
    position: absolute; left: 0; right: 0; top: 112px;
    display: flex; align-items: center; justify-content: center; gap: 14px;
  }
  .brand__mark { width: 26px; height: 26px; background: var(--green-text); }
  .brand__name {
    font-weight: 800; font-size: 46px; letter-spacing: 0.5px;
    color: var(--green-text); text-transform: uppercase; line-height: 1;
  }

  /* Back */
  .back .card__ghost { left: 330px; top: 30px; width: 260px; height: 250px; }
  .back .brand { left: 58px; right: auto; top: 58px; gap: 10px; }
  .back .brand__mark { width: 18px; height: 18px; }
  .back .brand__name { font-size: 30px; }
  .person {
    position: absolute; right: 44px; top: 90px; text-align: right;
  }
  .person__name { color: var(--green-text); font-size: 22px; font-weight: 400; letter-spacing: 0.5px; line-height: 1.3; }
  .person__title { color: var(--green-text); font-size: 15px; margin-top: 2px; }
  .info-strip {
    position: absolute; left: 0; right: 0; top: 178px; height: 104px;
    background: var(--strip-dark);
  }
  .back .card__band { height: 95px; }
  .contact-list {
    position: absolute; left: 58px; right: 30px; top: 200px;
    display: flex; gap: 40px;
    color: var(--white); font-size: 14.5px; line-height: 26px;
  }
  .contact--address { width: 196px; }
  .contact--phone { width: 130px; }
  .contact__row { display: flex; align-items: center; gap: 7px; white-space: nowrap; }
  .contact__row svg { width: 12px; height: 12px; fill: var(--green-text); flex: none; }
</style>
</head>
<body>
<main class="canvas">

  <section class="card front" aria-label="Business card front">
    <div class="card__ghost" role="img" aria-label="Faint silhouette of an athlete in motion"></div>
    <div class="brand">
      <span class="brand__mark"></span>
      <span class="brand__name">Kestrel Fitness</span>
    </div>
    <div class="card__band"></div>
  </section>

  <section class="card back" aria-label="Business card back">
    <div class="info-strip"></div>
    <div class="card__ghost" role="img" aria-label="Faint silhouette of an athlete in motion"></div>
    <div class="brand">
      <span class="brand__mark"></span>
      <span class="brand__name">Kestrel Fitness</span>
    </div>
    <div class="person">
      <p class="person__name">MARCUS HALE</p>
      <p class="person__title">Managing Director</p>
    </div>
    <div class="card__band"></div>

    <div class="contact-list">
      <div class="contact contact--address">
        <p class="contact__row">
          <svg viewBox="0 0 12 12"><path d="M6 0a4 4 0 0 0-4 4c0 3 4 8 4 8s4-5 4-8a4 4 0 0 0-4-4zm0 5.6A1.6 1.6 0 1 1 6 2.4a1.6 1.6 0 0 1 0 3.2z"/></svg>
          1234, Address Goes Here,
        </p>
        <p class="contact__row">Country Name, 123456</p>
      </div>

      <div class="contact contact--phone">
        <p class="contact__row">
          <svg viewBox="0 0 12 12"><path d="M1 4c0-2 2-3 5-3s5 1 5 3l-2 1-1-1.5H4L3 5zM3 6h6l1 5H2z"/></svg>
          123.456.7890
        </p>
        <p class="contact__row">
          <svg viewBox="0 0 12 12"><path d="M3 1h5l1 1v3H3zM1 5h10v6H1zm2 2v2h6V7z"/></svg>
          123.456.7890
        </p>
      </div>

      <div class="contact contact--web">
        <p class="contact__row">
          <svg viewBox="0 0 12 12"><path d="M0 2h12v8H0zm1 1v.5l5 3.2 5-3.2V3z"/></svg>
          info@youremail.com
        </p>
        <p class="contact__row">
          <svg viewBox="0 0 12 12"><path d="M5 7 7 5M4.5 4.5 6 3a2 2 0 0 1 3 3L7.5 7.5M7.5 7.5 6 9a2 2 0 0 1-3-3l1.5-1.5" stroke="#3dbd4c" stroke-width="1.4" fill="none"/></svg>
          www.website.com
        </p>
      </div>
    </div>
  </section>

</main>
</body>
</html>
```